Atelier Marrow Architecture business card

We need to update our business card. We do high end custom residential, hospitality, and wellness architecture. We focus on creating unique spaces and design around the five senses, believing that architecture's true impact is not on our surroundings, but within us. We would like to see designs are instill a sense of calm awe. They should be crisp, fresh, clean, authentic, & contemporary without being sterile, overworked, or harsh. White space is important. Alternative materials are an option if natural. We have created our own logo and would like designs to incorporate it. However, we are willing to see alternatives if the logo becomes a stumbling block and you have an alternate you suggest. Card must have the following information:
Atelier Marrow Architecture, Inc.
728 Holloway Ct. NE Atlanta, GA 30318
Marcus T. Whitcombe, AIA, NCARB, LEED AP BD+C
ateliermarrow.example

Target Market(s)

Higher net worth individuals with an appreciation for design, nature, sustainability,

Industry/Entity Type

Architect

Contact Information for Business Card

See above. The title of Owner or Architect is helpful but not necessary. Minimalism should trump additional information.

Font styles to use
Serif
Sans Serif

Requirements
Must have
• It should look professional. It must use logo
Should not have
• caligraphy, animals, anything that is cute,

```html
<!DOCTYPE html>
<html lang="en">
<head>
<meta charset="utf-8">
<title>Atelier Marrow Architecture — Business Card</title>
<link rel="stylesheet" href="https://fonts.googleapis.com/css2?family=Open+Sans:wght@400;600&display=swap">
<style>
  :root {
    --backdrop: #e9e6e2;
    --card: #ffffff;
    --ink: #3f3f3f;
    --ink-soft: #4a4a4a;
    --shadow: rgba(0, 0, 0, 0.28);
  }
  html, body {
    margin: 0;
    padding: 0;
    width: 1200px;
    height: 1000px;
    overflow: hidden;
    background: var(--backdrop);
    font-family: "Open Sans", Arial, sans-serif;
    color: var(--ink);
  }
  .canvas {
    position: relative;
    width: 1200px;
    height: 1000px;
  }
  .card {
    position: absolute;
    left: 266px;
    width: 666px;
    height: 397px;
    background: var(--card);
    box-shadow: 0 4px 10px var(--shadow);
  }
  .card--front { top: 74px; }
  .card--back  { top: 533px; }

  .wordmark {
    position: absolute;
    font-weight: 400;
    color: var(--ink);
    text-transform: uppercase;
    white-space: nowrap;
  }
  .card--front .wordmark {
    right: 32px;
    top: 58px;
    font-size: 17px;
    letter-spacing: 0.22em;
  }
  .card--back .wordmark {
    left: 0;
    right: 0;
    top: 178px;
    text-align: center;
    font-size: 24px;
    letter-spacing: 0.26em;
  }

  .contact {
    position: absolute;
    left: 33px;
    top: 156px;
  }
  .contact__name {
    margin: 0;
    font-size: 20px;
    font-weight: 600;
    line-height: 1.2;
    color: var(--ink);
  }
  .contact__credentials {
    margin: 2px 0 14px;
    font-size: 14.5px;
    color: var(--ink-soft);
  }
  .contact__list {
    list-style: none;
    margin: 0 0 8px;
    padding: 0;
    font-size: 15px;
    line-height: 21.5px;
    color: var(--ink-soft);
  }
  .contact__list li {
    display: flex;
    align-items: center;
    gap: 5px;
  }
  .contact__list svg {
    width: 16px;
    height: 14px;
    fill: var(--ink);
    flex: none;
  }
  .contact__company {
    margin: 0;
    font-size: 15px;
    font-weight: 600;
    color: var(--ink);
  }
  .contact__address {
    margin: 2px 0 0;
    font-size: 15px;
    line-height: 20px;
    font-style: normal;
    color: var(--ink-soft);
  }
</style>
</head>
<body>
<main class="canvas">
  <section class="card card--front" aria-label="Business card front">
    <div class="wordmark">Atelier Marrow Architecture</div>
    <div class="contact">
      <h1 class="contact__name">Marcus T. Whitcombe</h1>
      <p class="contact__credentials">AIA, NCARB, LEED AP BD+C</p>
      <ul class="contact__list">
        <li>
          <svg viewBox="0 0 16 14" aria-hidden="true"><path d="M1 4c0-2 3-3 7-3s7 1 7 3v1.5h-3.5V4h-7v1.5H1z"/><path d="M3 7h10l1.5 6h-13z"/></svg>
          404.555.0162
        </li>
        <li>
          <svg viewBox="0 0 16 14" aria-hidden="true"><rect x="4" y="0.5" width="8" height="4"/><rect x="1" y="5" width="14" height="6" rx="1"/><rect x="4" y="9" width="8" height="5" fill="#fff" stroke="#3f3f3f" stroke-width="1.2"/></svg>
          404.555.0178
        </li>
        <li>
          <svg viewBox="0 0 16 14" aria-hidden="true"><rect x="1" y="2" width="14" height="10"/><path d="M1.5 2.5L8 8l6.5-5.5" fill="none" stroke="#fff" stroke-width="1.3"/></svg>
          info@ateliermarrow.example
        </li>
        <li>
          <svg viewBox="0 0 16 14" aria-hidden="true"><circle cx="8" cy="7" r="6" fill="none" stroke="#3f3f3f" stroke-width="1.6"/><path d="M8 1v12M2 7h12" stroke="#3f3f3f" stroke-width="1.2"/></svg>
          ateliermarrow.example
        </li>
      </ul>
      <p class="contact__company">Atelier Marrow Architecture, Inc.</p>
      <address class="contact__address">728 Holloway Ct. NE Atlanta,<br>GA 30318</address>
    </div>
  </section>

  <section class="card card--back" aria-label="Business card back">
    <div class="wordmark">Atelier Marrow Architecture</div>
  </section>
</main>
</body>
</html>
```